PowerPoint template design needed for sales and presales presentations

We would like to have a bright and light, contemporary PowerPoint design based on our existing style assets (see attached files).
We are based in Latvia. Our business is ERP systems implementation, IT infrastructure building and supporting our customers. We are moving from traditional Add-hoc projects model to standardized flat-rate offerings. Our technology platform is Quintavel.
The value proposition of our offerings is based around simplicity, transparency, quality, peace of mind, trust, easy of doing business.
I have to add that if any special are being used, they must be unicode to ensure proper Latvian language characters display.
Updates
Hi! The reason is an error at your side. Today it's 24/08/2020 when I started the project and made a payment. Still for some funny reason in the BRIEF I see that the project deadline is set to 20/08/2020. No wonder no designers are applying...
Target Market(s)
Small and medium enterprise
Look and feel

```html
<!DOCTYPE html>
<html lang="en">
<head>
<meta charset="utf-8">
<title>Veltrano – Presentation Template</title>
<link href="https://fonts.googleapis.com/css2?family=Montserrat:wght@400;500;600;700&display=swap" rel="stylesheet">
<style>
  :root{
    --teal:#00b9b4;
    --green:#8cc63f;
    --yellow:#ffc30f;
    --navy:#1c1a4d;
    --ink:#222;
    --grey-text:#9a9a9a;
    --panel:#f1f1f1;
    --board:#878787;
    --white:#fff;
  }
  *{box-sizing:border-box;margin:0;padding:0}
  html,body{width:674px;height:1200px;overflow:hidden;background:var(--board)}
  body{font-family:"Montserrat",Arial,sans-serif;color:var(--ink)}
  .canvas{position:relative;width:674px;height:1200px;overflow:hidden;background:var(--board)}
  .board{position:absolute;left:0;top:0;width:1447px;height:2576px;transform:scale(0.46579);transform-origin:0 0}
  .slide{position:absolute;width:646px;height:363px;background:var(--white);overflow:hidden}
  .col-a{left:59px}.col-b{left:748px}
  .abs{position:absolute}

  /* colour strip */
  .strip{position:absolute;display:flex;gap:4px;height:18px}
  .strip span{display:block;width:65px;height:100%}
  .strip .t{background:var(--teal)}.strip .g{background:var(--green)}.strip .y{background:var(--yellow)}

  /* brand name */
  .brand{position:absolute;display:flex;align-items:center}
  .brand .name{font-weight:600;color:var(--navy);line-height:1;white-space:nowrap}
  .brand.small{right:14px;top:20px}
  .brand.small .name{font-size:10px;letter-spacing:1.5px}
  .brand.cover{left:0;right:0;top:166px;justify-content:center}
  .brand.cover .name{color:var(--white);font-size:24px;letter-spacing:5px}
  .brand.light .name{color:var(--white)}

  .cover-rule{position:absolute;left:231px;top:242px;width:185px;height:2px;background:linear-gradient(90deg,transparent,rgba(10,40,70,.8),transparent)}
  .menu-grid{position:absolute;right:10px;top:9px;width:19px;height:19px;display:grid;grid-template-columns:repeat(3,1fr);gap:2px}
  .menu-grid i{background:var(--white)}
  .social{position:absolute;left:7px;top:346px;display:flex;gap:3px}
  .social i{width:8px;height:8px;background:var(--white)}

  .photo{position:absolute}
  .ph-steel{background:linear-gradient(135deg,#0e2a38 0%,#4d7d92 45%,#a9c6d1 70%,#1c3a48 100%)}
  .ph-glass{background:linear-gradient(160deg,#2a3a44 0%,#7c8b93 40%,#1a2228 60%,#cfd6d9 100%)}
  .ph-city{background:linear-gradient(180deg,#6c7a84 0%,#47535b 40%,#2a3036 75%,#3c3f42 100%)}
  .ph-data{background:linear-gradient(120deg,#0f2b3f 0%,#2f6f8f 45%,#8fc6dc 60%,#15324a 100%)}
  .ph-tech{background:linear-gradient(90deg,#d7e3ee 0%,#3b83c4 30%,#1c4f8c 55%,#6f9ecb 80%,#e3e8ec 100%)}
  .ph-mono{background:linear-gradient(150deg,#e7e7e7 0%,#9a9a9a 40%,#3d3d3d 70%,#777 100%)}
  .ph-night{background:linear-gradient(160deg,#2a2233 0%,#6c5b72 35%,#c7a77a 55%,#2b2431 100%)}

  .h-big{font-weight:500;font-size:28px;line-height:1.15;color:var(--navy)}
  .h-white{color:var(--white)}
  .t-label{font-weight:700;font-size:9px;color:var(--navy)}
  .t-spaced{font-weight:700;font-size:10px;letter-spacing:4px;color:var(--navy)}
  .copy{font-size:6.5px;line-height:1.55;color:var(--grey-text)}
  .copy.j{text-align:justify}

  .tag{position:absolute;display:flex;align-items:center;color:var(--white);font-weight:500;font-size:28px}
  .bar-bottom{position:absolute;display:flex;gap:4px;right:0;bottom:0;height:15px}
  .bar-bottom span{width:65px;height:100%}
  .bar-bottom .t{background:var(--teal)}.bar-bottom .g{background:var(--green)}.bar-bottom .y{background:var(--yellow)}

  .icon{position:absolute;width:22px;height:22px;stroke:var(--navy);fill:none;stroke-width:1.8}
  .tile{position:absolute;top:277px;width:106px;height:52px;background:var(--panel);text-align:center;padding-top:8px}
  .tile .t-label{font-size:8px}
  .tile .copy{font-size:5.5px;margin-top:4px}
</style>
</head>
<body>
<div class="canvas">
 <div class="board">

  <!-- cover teal -->
  <section class="slide col-a" style="top:48px;background:var(--teal)">
    <div class="menu-grid"><i></i><i></i><i></i><i></i><i></i><i></i><i></i><i></i><i></i></div>
    <div class="brand cover"><span class="name">VELTRANO</span></div>
    <div class="cover-rule"></div>
    <div class="social"><i></i><i></i><i></i><i></i></div>
  </section>

  <!-- cover dark -->
  <section class="slide col-b" style="top:48px;background:radial-gradient(ellipse at 50% 40%,#155a8e 0%,#0a3a66 55%,#06213d 100%)" role="img" aria-label="Deep blue textured cover background">
    <div class="menu-grid"><i></i><i></i><i></i><i></i><i></i><i></i><i></i><i></i><i></i></div>
    <div class="brand cover"><span class="name">VELTRANO</span></div>
    <div class="cover-rule" style="background:linear-gradient(90deg,transparent,rgba(120,170,210,.5),transparent)"></div>
    <div class="social"><i></i><i></i><i></i><i></i></div>
  </section>

  <!-- content -->
  <section class="slide col-a" style="top:470px">
    <div class="strip" style="left:0;top:0"><span class="t"></span><span class="g"></span><span class="y"></span></div>
    <div class="photo ph-steel" style="left:0;top:18px;width:204px;height:345px" role="img" aria-label="Curved glass lattice architecture photo"></div>
    <div class="brand small"><span class="name">VELTRANO</span></div>
    <div class="tag" style="left:234px;top:51px;width:412px;height:49px;background:var(--teal);padding-left:14px">content</div>
    <p class="copy abs" style="left:248px;top:137px;width:320px">Nullam eu tempor purus. Nunc a leo magna, sit amet consequat risus. Etiam faucibus tortor a ipsum vehicula sed hendrerit eros suscipit. Vestibulum neque elit, Class aptent taciti sociosqu ad litora torquent per conubia nostra, per inceptos himenaeos. Nullam eu tempor purus. Nunc a leo magna, sit amet consequat risus. Etiam faucibus tortor a ipsum vehicula sed hendrerit eros suscipit.</p>
    <svg class="icon" style="left:285px;top:227px" viewBox="0 0 24 24"><rect x="3" y="4" width="18" height="12"/><path d="M12 16v4M8 20h8"/></svg>
    <svg class="icon" style="left:410px;top:227px" viewBox="0 0 24 24"><circle cx="12" cy="12" r="9"/><path d="M3 12h18M12 3c3 3 3 15 0 18M12 3c-3 3-3 15 0 18"/></svg>
    <svg class="icon" style="left:535px;top:227px;fill:var(--navy)" viewBox="0 0 24 24"><circle cx="10" cy="14" r="6"/><circle cx="19" cy="6" r="3"/></svg>
    <div class="tile" style="left:243px"><div class="t-label">title</div><p class="copy">Nullam eu tempor purus.<br>Nunc a leo magna.</p></div>
    <div class="tile" style="left:368px"><div class="t-label">title</div><p class="copy">Nullam eu tempor purus.<br>Nunc a leo magna.</p></div>
    <div class="tile" style="left:493px"><div class="t-label">title</div><p class="copy">Nullam eu tempor purus.<br>Nunc a leo magna.</p></div>
  </section>

  <!-- about slide list -->
  <section class="slide col-b" style="top:475px">
    <div class="strip" style="left:0;top:0"><span class="t"></span><span class="g"></span><span class="y"></span></div>
    <div class="brand small"><span class="name">VELTRANO</span></div>
    <h2 class="h-big abs" style="left:23px;top:48px">about slide</h2>
    <div class="t-label abs" style="left:224px;top:41px">write title here</div>
    <p class="copy abs" style="left:224px;top:54px;width:340px">Nullam eu tempor purus. Nunc a leo magna, sit amet consequat risus. Etiam faucibus tortor a ipsum vehicula sed hendrerit eros suscipit. Vestibulum neque elit, Class aptent taciti sociosqu ad litora torquent per conubia nostra, per inceptos himenaeos.</p>
    <div class="photo ph-data" style="left:18px;top:112px;width:275px;height:216px" role="img" aria-label="Businessman facing a wall of data screens"></div>
    <svg class="icon" style="left:340px;top:139px;width:18px;height:18px" viewBox="0 0 24 24"><rect x="5" y="11" width="14" height="10"/><path d="M8 11V7a4 4 0 0 1 8 0v4"/></svg>
    <div class="t-label abs" style="left:372px;top:143px">write title here</div>
    <p class="copy abs" style="left:340px;top:168px;width:260px">Nullam eu tempor purus. Nunc a leo magna, sit amet consequat risus. Etiam faucibus tortor a ipsum vehicula sed hendrerit eros suscipit.</p>
    <svg class="icon" style="left:340px;top:195px;width:18px;height:18px" viewBox="0 0 24 24"><path d="M4 16v-4a8 8 0 0 1 16 0v4"/><rect x="3" y="14" width="4" height="6"/><rect x="17" y="14" width="4" height="6"/></svg>
    <div class="t-label abs" style="left:372px;top:199px">write title here</div>
    <p class="copy abs" style="left:340px;top:223px;width:260px">Nullam eu tempor purus. Nunc a leo magna, sit amet consequat risus. Etiam faucibus tortor a ipsum vehicula sed hendrerit eros suscipit.</p>
    <svg class="icon" style="left:340px;top:253px;width:18px;height:18px" viewBox="0 0 24 24"><path d="M20 12a8 8 0 0 1-14 5M4 12a8 8 0 0 1 14-5"/><path d="M18 3v4h-4M6 21v-4h4"/></svg>
    <div class="t-label abs" style="left:372px;top:257px">write title here</div>
    <p class="copy abs" style="left:340px;top:280px;width:260px">Nullam eu tempor purus. Nunc a leo magna, sit amet consequat risus. Etiam faucibus tortor a ipsum vehicula sed hendrerit eros suscipit.</p>
    <div class="abs" style="left:0;top:350px;width:646px;height:13px;background:var(--teal)"></div>
  </section>

  <!-- welcome 1 -->
  <section class="slide col-a" style="top:891px">
    <div class="brand small"><span class="name">VELTRANO</span></div>
    <div class="photo ph-glass" style="left:50px;top:53px;width:545px;height:196px" role="img" aria-label="Glass roof seen from below"></div>
    <div class="tag" style="left:0;top:149px;width:180px;height:48px;background:var(--green);padding-left:30px">welcome</div>
    <div class="t-spaced abs" style="left:55px;top:263px">write title here</div>
    <p class="copy j abs" style="left:55px;top:279px;width:195px">Nullam eu tempor purus. Nunc a leo magna, sit amet consequat risus. Etiam faucibus tortor a ipsum vehicula sed hendrerit eros suscipit. Vestibulum neque elit, Class aptent taciti sociosqu ad litora torquent per conubia nostra, per inceptos himenaeos. Nullam eu tempor purus. Nunc a leo magna.</p>
    <p class="copy j abs" style="left:272px;top:279px;width:195px">Nullam eu tempor purus. Nunc a leo magna, sit amet consequat risus. Etiam faucibus tortor a ipsum vehicula sed hendrerit eros suscipit. Vestibulum neque elit, Class aptent taciti sociosqu ad litora torquent per conubia nostra, per inceptos himenaeos. Nullam eu tempor purus. Nunc a leo magna.</p>
    <p class="copy j abs" style="left:489px;top:279px;width:120px">Nullam eu tempor purus. Nunc a leo magna, sit amet consequat risus. Etiam faucibus tortor a ipsum vehicula sed hendrerit eros suscipit. Vestibulum neque elit, Class aptent taciti sociosqu</p>
  </section>

  <!-- about slide 2 -->
  <section class="slide col-b" style="top:894px">
    <div class="photo ph-steel" style="left:0;top:0;width:240px;height:363px" role="img" aria-label="Glass skyscraper facade photo"></div>
    <div class="abs" style="left:9px;top:9px;width:184px;height:250px;background:linear-gradient(180deg,#0e3c6e 0%,#1e1548 100%)">
      <p class="abs" style="left:30px;top:67px;width:124px;font-size:6.5px;line-height:1.55;color:var(--white);text-align:center">Nullam eu tempor purus. Nunc a leo magna, sit amet consequat risus. Etiam faucibus tortor a ipsum vehicula sed hendrerit eros suscipit. Vestibulum neque elit, Class aptent taciti sociosqu ad litora torquent per conubia nostra, per inceptos himenaeos.</p>
      <svg class="abs" style="left:63px;top:167px;width:58px;height:50px" viewBox="0 0 58 50" fill="#fff"><rect x="0" y="0" width="16" height="50"/><rect x="21" y="0" width="16" height="50"/><rect x="42" y="0" width="16" height="50"/><g fill="#1e1548"><rect x="3" y="8" width="10" height="4"/><rect x="24" y="8" width="10" height="4"/><rect x="45" y="8" width="10" height="4"/><circle cx="8" cy="38" r="3"/><circle cx="29" cy="38" r="3"/><circle cx="50" cy="38" r="3"/></g></svg>
    </div>
    <div class="brand small"><span class="name">VELTRANO</span></div>
    <h2 class="h-big abs" style="left:315px;top:78px">about slide</h2>
    <p class="copy abs" style="left:315px;top:134px;width:255px">Nullam eu tempor purus. Nunc a leo magna, sit amet consequat risus. Etiam faucibus tortor a ipsum vehicula sed hendrerit eros suscipit. Vestibulum neque elit, Class aptent taciti sociosqu ad litora torquent per conubia nostra, per inceptos himenaeos.</p>
    <div class="t-label abs" style="left:315px;top:228px">write title here</div>
    <p class="copy abs" style="left:315px;top:243px">Nullam eu tempor purus.<br>Nunc a leo magna, sit amet.</p>
    <div class="t-label abs" style="left:463px;top:228px">write title here</div>
    <p class="copy abs" style="left:463px;top:243px">Nullam eu tempor purus.<br>Nunc a leo magna, sit amet.</p>
    <div class="t-label abs" style="left:315px;top:286px">write title here</div>
    <p class="copy abs" style="left:315px;top:301px">Nullam eu tempor purus.<br>Nunc a leo magna, sit amet.</p>
    <div class="t-label abs" style="left:463px;top:286px">write title here</div>
    <p class="copy abs" style="left:463px;top:301px">Nullam eu tempor purus.<br>Nunc a leo magna, sit amet.</p>
    <div class="bar-bottom"><span class="t"></span><span class="g"></span><span class="y"></span></div>
  </section>

  <!-- welcome message -->
  <section class="slide col-a" style="top:1313px">
    <div class="photo ph-city" style="left:17px;top:0;width:245px;height:363px" role="img" aria-label="City skyline with a tall tower under storm clouds"></div>
    <div class="brand small"><span class="name">VELTRANO</span></div>
    <div class="tag" style="left:263px;top:86px;width:169px;height:48px;background:var(--yellow);padding-left:19px">welcome</div>
    <h2 class="h-big abs" style="left:282px;top:136px">message</h2>
    <div class="t-spaced abs" style="left:337px;top:218px">write title here</div>
    <p class="copy abs" style="left:337px;top:239px;width:275px">Nullam eu tempor purus. Nunc a leo magna, sit amet consequat risus. Etiam faucibus tortor a ipsum vehicula sed hendrerit eros suscipit. Vestibulum neque elit, Class aptent taciti sociosqu ad litora torquent per conubia nostra, per inceptos himenaeos. Nullam eu tempor purus. Nunc a leo magna, sit amet consequat risus. Etiam faucibus tortor a ipsum vehicula sed hendrerit eros suscipit. Vestibulum neque elit, Class aptent taciti sociosqu ad litora torquent per conubia nostra, per inceptos himenaeos.</p>
    <div class="bar-bottom" style="height:18px"><span class="t"></span><span class="g"></span><span class="y"></span></div>
  </section>

  <!-- overview 1 -->
  <section class="slide col-b" style="top:1313px">
    <div class="strip" style="left:0;top:0"><span class="t"></span><span class="g"></span><span class="y"></span></div>
    <div class="brand small"><span class="name">VELTRANO</span></div>
    <div class="abs" style="left:0;top:52px;width:17px;height:57px;background:var(--navy)"></div>
    <h2 class="h-big abs" style="left:53px;top:64px">overview</h2>
    <div class="t-label abs" style="left:221px;top:41px">write title here</div>
    <p class="copy abs" style="left:221px;top:67px;width:380px">Nullam eu tempor purus. Nunc a leo magna, sit amet consequat risus. Etiam faucibus tortor a ipsum vehicula sed hendrerit eros suscipit. Vestibulum neque elit, Class aptent taciti sociosqu ad litora torquent per conubia nostra, per inceptos himenaeos. Nullam eu tempor purus. Nunc a leo magna, sit amet consequat risus. Etiam faucibus tortor a ipsum vehicula sed hendrerit eros suscipit. Vestibulum neque elit, Class aptent taciti sociosqu ad litora torquent per conubia nostra, per inceptos himenaeos.</p>
    <div class="photo ph-tech" style="left:0;top:149px;width:646px;height:214px" role="img" aria-label="Hand touching a glowing network of app icons around a globe"></div>
  </section>

  <!-- about banner -->
  <section class="slide col-a" style="top:1735px">
    <div class="photo ph-data" style="left:0;top:0;width:646px;height:215px" role="img" aria-label="Businesswoman viewing large digital dashboards"></div>
    <div class="brand small light"><span class="name">VELTRANO</span></div>
    <div class="abs" style="left:25px;top:178px;width:203px;height:117px;background:var(--teal)">
      <div class="abs h-white" style="left:34px;top:12px;font-size:28px;font-weight:500">about</div>
      <svg class="abs" style="left:179px;top:7px;width:16px;height:16px" viewBox="0 0 16 16" stroke="#fff" stroke-width="2"><path d="M8 1v14M1 8h14"/></svg>
      <div class="abs" style="left:34px;top:88px;font-size:9px;font-weight:700;color:var(--white)">write title here</div>
    </div>
    <p class="copy abs" style="left:258px;top:260px;width:345px">Nullam eu tempor purus. Nunc a leo magna, sit amet consequat risus. Etiam faucibus tortor a ipsum vehicula sed hendrerit eros suscipit. Vestibulum neque elit, Class aptent taciti sociosqu ad litora torquent per conubia nostra, per inceptos himenaeos. Nullam eu tempor purus. Nunc a leo magna, sit amet consequat risus. Etiam faucibus tortor a ipsum vehicula sed hendrerit eros suscipit. Vestibulum neque elit, Class aptent taciti sociosqu ad litora torquent per conubia nostra, per inceptos himenaeos.</p>
  </section>

  <!-- overview slide lock -->
  <section class="slide col-b" style="top:1735px">
    <div class="photo ph-city" style="left:0;top:0;width:262px;height:363px" role="img" aria-label="City skyline with a tall tower under storm clouds"></div>
    <div class="abs" style="left:226px;top:144px;width:72px;height:72px;border-radius:50%;background:radial-gradient(circle at 40% 35%,#3a2f7a,var(--navy));display:flex;align-items:center;justify-content:center">
      <svg width="22" height="26" viewBox="0 0 22 26" fill="none" stroke="#fff" stroke-width="2"><rect x="2" y="11" width="18" height="13"/><path d="M6 11V7a5 5 0 0 1 10 0v4M11 16v3"/></svg>
    </div>
    <div class="brand small"><span class="name">VELTRANO</span></div>
    <h2 class="h-big abs" style="left:346px;top:96px">overview<br>slide</h2>
    <div class="t-label abs" style="left:346px;top:207px">write title here</div>
    <p class="copy abs" style="left:346px;top:234px;width:252px">Nullam eu tempor purus. Nunc a leo magna, sit amet consequat risus. Etiam faucibus tortor a ipsum vehicula sed hendrerit eros suscipit. Vestibulum neque elit, Class aptent taciti sociosqu ad litora torquent per conubia nostra, per inceptos himenaeos. Nullam eu tempor purus. Nunc a leo magna, sit amet consequat risus. Etiam faucibus tortor a ipsum vehicula sed hendrerit eros suscipit. Vestibulum neque elit, Class aptent taciti sociosqu ad litora torquent per conubia nostra, per inceptos himenaeos.</p>
    <div class="bar-bottom"><span class="t"></span><span class="g"></span><span class="y"></span></div>
  </section>

  <!-- title space -->
  <section class="slide col-a" style="top:2156px">
    <div class="strip" style="left:0;top:0"><span class="t"></span><span class="g"></span><span class="y"></span></div>
    <div class="brand small"><span class="name">VELTRANO</span></div>
    <div class="t-label abs" style="left:44px;top:59px">write title here</div>
    <p class="copy abs" style="left:44px;top:75px;width:200px">Nullam eu tempor purus. Nunc a leo magna, sit amet consequat risus. Etiam faucibus tortor a ipsum vehicula sed hendrerit eros suscipit. Vestibulum neque elit, Class aptent taciti sociosqu ad litora torquent per conubia nostra, per inceptos himenaeos.</p>
    <div class="t-label abs" style="left:44px;top:140px">write title here</div>
    <p class="copy abs" style="left:44px;top:156px;width:200px">Nullam eu tempor purus. Nunc a leo magna, sit amet consequat risus. Etiam faucibus tortor a ipsum vehicula sed hendrerit eros suscipit. Vestibulum neque elit, Class aptent taciti sociosqu ad litora torquent per conubia nostra, per inceptos himenaeos.</p>
    <div class="t-label abs" style="left:44px;top:222px">write title here</div>
    <p class="copy abs" style="left:44px;top:238px;width:200px">Nullam eu tempor purus. Nunc a leo magna, sit amet consequat risus. Etiam faucibus tortor a ipsum vehicula sed hendrerit eros suscipit. Vestibulum neque elit, Class aptent taciti sociosqu ad litora torquent per conubia nostra, per inceptos himenaeos.</p>
    <div class="photo ph-mono" style="left:292px;top:50px;width:308px;height:279px" role="img" aria-label="Black and white skyscrapers against a cloudy sky"></div>
    <div class="abs" style="left:353px;top:277px;width:185px;height:70px;background:var(--green);display:flex;align-items:center;justify-content:center;text-align:center;font-size:26px;font-weight:500;line-height:1.2;color:var(--navy)">TITLE<br>SPACE</div>
  </section>

  <!-- overview slide 3 -->
  <section class="slide col-b" style="top:2152px">
    <div class="strip" style="left:0;top:0"><span class="t"></span><span class="g"></span><span class="y"></span></div>
    <div class="t-label abs" style="left:37px;top:66px">write title here</div>
    <p class="copy abs" style="left:37px;top:92px;width:200px">Nullam eu tempor purus. Nunc a leo magna, sit amet consequat risus. Etiam faucibus tortor a ipsum vehicula sed hendrerit eros suscipit. Vestibulum neque elit, Class aptent taciti sociosqu ad litora torquent per conubia nostra, per inceptos himenaeos. Nullam eu tempor purus. Nunc a leo magna, sit amet consequat risus. Etiam faucibus tortor a ipsum vehicula sed hendrerit eros suscipit. Vestibulum neque elit, Class aptent taciti sociosqu ad litora torquent per conubia nostra, per inceptos himenaeos.</p>
    <h2 class="h-big abs" style="left:37px;top:236px">overview<br>slide</h2>
    <div class="abs" style="left:0;top:326px;width:163px;height:8px;background:var(--navy)"></div>
    <div class="t-label abs" style="left:329px;top:50px">write title here</div>
    <p class="copy abs" style="left:329px;top:66px">Nullam eu tempor purus.<br>Nunc a leo magna, sit amet.</p>
    <div class="t-label abs" style="left:477px;top:50px">write title here</div>
    <p class="copy abs" style="left:477px;top:66px">Nullam eu tempor purus.<br>Nunc a leo magna, sit amet.</p>
    <div class="photo ph-night" style="left:293px;top:125px;width:337px;height:220px" role="img" aria-label="Skyscrapers seen from below at dusk"></div>
  </section>

 </div>
</div>
</body>
</html>
```